Quorvel Marketing & Design needs a Wordpress website

We need a wordpress design for a new marketing and design company in Australia called 'Quorvel Marketing & Design". The website needs to be responsive, modern, and attract new customers. It needs to be unique and different. We provide marketing and design solutions for small businesses from consulting, to flyer distribution to Facebook ads etc. We would like to see designs that use the Quorvel logo colours. The final design should communicate professionalism, creativity & growth. It needs to stand out from the crowd.

Target Market(s)

Small Business who need a marketing freelancer to help them grow

Industry/Entity Type

Marketing

Number of Pages Required

3 page

Requirements
Must have
• Home page, services page & contact page

```html
<!DOCTYPE html>
<html lang="en">
<head>
<meta charset="utf-8">
<title>Quorvel Marketing &amp; Design</title>
<link href="https://fonts.googleapis.com/css2?family=Open+Sans:wght@400;600;700&display=swap" rel="stylesheet">
<style>
:root{
  --pink:#d4156e;
  --pink-dark:#b10e5a;
  --ink:#2e2e2e;
  --grey:#6b6b6b;
  --light:#f4f4f4;
  --dark:#353535;
  --white:#fff;
}
*{margin:0;padding:0;box-sizing:border-box}
html,body{width:1200px;height:2304px;overflow:hidden}
body{font-family:"Open Sans",Arial,sans-serif;color:var(--ink);background:var(--white);position:relative}
.site-header{height:62px;display:flex;align-items:center;justify-content:space-between;padding:0 40px 0 30px;background:var(--white)}
.brand{display:flex;align-items:center;gap:10px}
.brand-dot{width:40px;height:40px;border-radius:50%;background:var(--pink)}
.brand-name{font-size:22px;font-weight:700;color:var(--pink)}
.main-nav{display:flex;gap:0}
.main-nav a{font-size:14px;color:var(--ink);text-decoration:none;padding:20px 24px;border-bottom:3px solid transparent}
.main-nav a.active{border-bottom-color:var(--pink)}
.hero{position:relative;height:520px;overflow:hidden}
.hero-photo{position:absolute;inset:0;background:linear-gradient(90deg,#eef0f2 0%,#e3e6ea 45%,#c9ced6 62%,#596070 78%,#e6e7ea 100%)}
.hero-copy{position:absolute;left:30px;top:52px;width:480px}
.hero-kicker{font-size:52px;font-weight:700;color:var(--pink);line-height:1.1}
.hero-title{font-size:40px;font-weight:700;color:var(--pink);line-height:1.2;margin-bottom:10px}
.hero-text{font-size:15px;line-height:1.5;color:var(--ink);margin-bottom:20px}
.btn-dark{display:inline-block;background:var(--dark);color:var(--white);font-size:14px;padding:10px 30px;border-radius:20px}
.services{padding:48px 0 60px;text-align:center}
.section-title{font-size:34px;font-weight:600;color:var(--ink)}
.title-rule{width:60px;height:3px;background:var(--pink);margin:12px auto 18px}
.section-sub{font-size:13px;color:var(--grey)}
.service-grid{display:flex;justify-content:center;gap:60px;margin-top:40px}
.service{width:300px}
.service-icon{width:76px;height:76px;border-radius:50%;background:var(--pink);margin:0 auto 22px;display:flex;align-items:center;justify-content:center}
.service h3{font-size:17px;font-weight:600;margin-bottom:14px}
.service p{font-size:12px;line-height:1.7;color:var(--grey);margin-bottom:18px}
.read-more{font-size:11px;font-weight:700;color:var(--pink);letter-spacing:.5px}
.welcome{position:relative;height:330px;background:linear-gradient(180deg,#3a3a3a,#2b2b2b);color:var(--white);text-align:center;padding-top:36px}
.welcome h2{font-size:34px;font-weight:600}
.welcome .title-rule{margin:10px auto 16px}
.welcome p{font-size:13px;line-height:1.6;width:720px;margin:0 auto 14px}
.testimonials{text-align:center;padding:44px 0 0;height:548px}
.testimonials .section-sub{font-size:22px;color:#8a8a8a}
.quote-badge{width:80px;height:80px;border-radius:50%;background:var(--pink);margin:48px auto 40px;display:flex;align-items:center;justify-content:center}
.quote-text{font-size:13px;line-height:1.7;color:var(--grey);width:800px;margin:0 auto 20px}
.quote-name{font-size:12px;font-weight:700}
.quote-meta{font-size:12px;font-weight:700;color:var(--ink)}
.site-footer{position:absolute;left:0;top:2020px;width:1200px;height:260px;background:var(--pink);color:var(--white);display:flex;padding:26px 30px 0;gap:40px}
.footer-col h4{font-size:19px;font-weight:600;margin-bottom:14px}
.footer-col ul{list-style:none}
.footer-col li{font-size:12px;margin-bottom:8px}
.footer-col li::before{content:"› ";}
.col-links{width:120px}.col-services{width:270px}.col-contact{width:330px}.col-news{width:300px}
.phone{display:flex;align-items:center;gap:10px;font-size:22px;margin-bottom:16px}
.chat-row{display:flex;align-items:center;gap:8px}
.chat-btn{background:var(--white);color:var(--pink);font-size:11px;font-weight:600;padding:5px 12px;border-radius:3px}
.social{width:22px;height:22px;border-radius:50%;background:var(--white)}
.field{width:300px;height:24px;background:var(--white);border-radius:2px;margin-bottom:8px;font-size:11px;color:#999;padding:4px 8px}
.field.tall{height:48px}
.btn-submit{background:var(--pink-dark);font-size:11px;padding:5px 14px;border-radius:2px;float:right;margin-right:0}
.copyright{position:absolute;left:0;top:2280px;width:1200px;height:24px;background:var(--pink-dark);color:var(--white);font-size:11px;text-align:center;line-height:24px}
</style>
</head>
<body>
<header class="site-header">
  <div class="brand"><span class="brand-dot"></span><span class="brand-name">Quorvel</span></div>
  <nav class="main-nav">
    <a class="active">Home</a><a>About Us</a><a>Services</a><a>Clients</a><a>Contact page</a>
  </nav>
</header>

<section class="hero">
  <div class="hero-photo" role="img" aria-label="Businessman in a suit reading a tablet in a bright office"></div>
  <div class="hero-copy">
    <div class="hero-kicker">Need help?</div>
    <div class="hero-title">Quorvel Marketing &amp; Design</div>
    <p class="hero-text">Grow steadily, let our friendly team handle your marketing with clear plans, fresh design and honest advice, so you can focus on running your business.</p>
    <span class="btn-dark">Read more ›</span>
  </div>
</section>

<section class="services">
  <h2 class="section-title">Our Services</h2>
  <div class="title-rule"></div>
  <p class="section-sub">In each of the three levels a package and a consult option</p>
  <div class="service-grid">
    <div class="service">
      <div class="service-icon"><svg width="40" height="40" viewBox="0 0 40 40"><path d="M8 28 L18 18 L24 24 L33 12" stroke="#fff" stroke-width="4" fill="none"/></svg></div>
      <h3>Just starting up?</h3>
      <p>Starting a business means a hundred jobs at once. We build your brand, your first flyers and a simple online presence so new customers can find you quickly and trust you from day one.</p>
      <span class="read-more">READ MORE</span>
    </div>
    <div class="service">
      <div class="service-icon"><svg width="40" height="40" viewBox="0 0 40 40"><path d="M20 6 L20 34 M8 20 L20 6 L32 20" stroke="#fff" stroke-width="4" fill="none"/></svg></div>
      <h3>Need a marketing boost or revamp</h3>
      <p>Already running but sales feel flat? We review what you have, refresh your look, plan social ads and flyer drops, and track the results so every dollar you spend keeps working harder.</p>
      <span class="read-more">READ MORE</span>
    </div>
    <div class="service">
      <div class="service-icon"><svg width="40" height="40" viewBox="0 0 40 40"><circle cx="20" cy="20" r="12" stroke="#fff" stroke-width="4" fill="none"/><circle cx="20" cy="20" r="4" fill="#fff"/></svg></div>
      <h3>Marketing Consulting or Advise</h3>
      <p>Prefer to do it yourself? Book a session and we share practical advice on strategy, branding and channels, giving you a clear plan and the confidence to carry it out in your own time.</p>
      <span class="read-more">READ MORE</span>
    </div>
  </div>
</section>

<section class="welcome" role="img" aria-label="Dark office scene behind the welcome message">
  <h2>Welcome to our website</h2>
  <div class="title-rule"></div>
  <p>Simple ideas, smart design and steady growth for small businesses.<br>Friendly help, real results.</p>
  <p>Looking for some marketing expertise or have you started your own business and ready to take the plunge in getting your name out there? You've come to the right place!</p>
  <p>It might just be that you want some solid marketing advice and then do it yourself or you might want us to help you out. Whatever you decide is fine by us, and we're always here to help.</p>
  <p>Here at Quorvel, we understand that each business is unique. That's why we offer tailored marketing and design services that are right for you and your business.</p>
</section>

<section class="testimonials">
  <h2 class="section-title">Testimonials</h2>
  <div class="title-rule"></div>
  <p class="section-sub">For more information on our services please click on the links below.</p>
  <div class="quote-badge"><svg width="34" height="28" viewBox="0 0 34 28"><path d="M2 16 Q2 4 13 2 L13 7 Q8 9 8 14 L14 14 L14 26 L2 26 Z M19 16 Q19 4 30 2 L30 7 Q25 9 25 14 L31 14 L31 26 L19 26 Z" fill="#fff"/></svg></div>
  <p class="quote-text">A wonderful team that took the time to understand my small studio. Our new flyers and social ads brought in more bookings within weeks, and the advice was clear and honest. I would recommend them to anyone starting out or wanting to grow.</p>
  <div class="quote-name">MAYA LIND</div>
  <div class="quote-meta">YOGA, 4 months</div>
</section>

<footer class="site-footer">
  <div class="footer-col col-links">
    <h4>LINKS</h4>
    <ul><li>Home</li><li>About Us</li><li>Services</li><li>Clients</li><li>Contact us</li></ul>
  </div>
  <div class="footer-col col-services">
    <h4>SERVICES</h4>
    <ul><li>Just starting up?</li><li>Need a marketing boost or revamp?</li><li>Marketing Consulting or Advise</li></ul>
  </div>
  <div class="footer-col col-contact">
    <h4>CONTACT US</h4>
    <div class="phone"><svg width="22" height="22" viewBox="0 0 24 24"><path d="M6 2 L10 6 L8 9 Q10 14 15 16 L18 14 L22 18 L19 22 Q8 20 2 5 Z" fill="#fff"/></svg>+61 2 5550 1040</div>
    <div class="chat-row"><span class="chat-btn">Live Chat - Online Now</span><span class="social"></span><span class="social"></span><span class="social"></span><span class="social"></span></div>
  </div>
  <div class="footer-col col-news">
    <h4>NEWSLETTER SIGN UP</h4>
    <div class="field">Name</div>
    <div class="field">Email</div>
    <div class="field tall">Message</div>
    <span class="btn-submit">Submit</span>
  </div>
</footer>
<div class="copyright">Copyright © 2016 Quorvel Marketing &amp; Design. All rights reserved.</div>
</body>
</html>
```